Escape Room Flyer Design - Start up. A5

Flyer is for letterbox drops to get interest and let people know that our business exists and to a lesser extent what an escape room is. We have 1 room (the miller's shadows) and a second room coming soon (Varuna's Vault). I have attached our logo and 2 flyers that I have seen in the past that I really like the design of.
Whether you are having a night out with friends or family, celebrating a special event, planning a team-building activity, or simply wanting a diversion from the doldrums of your workweek, The Lock Box will provide you an unforgettable live-action gaming experience.

Target Market(s)

18-25

Industry/Entity Type

Entertainment

Requirements
Must have
• Logo. Phone number 0417 265 839. Website. www.thelockboxhartwell.com
Bookings essential.
Nice to have
• Mystery, a little bit on the darker side than bright colourful and blocky.
"Many Will Enter…Few Will Escape" tag line
60 minute game. Team work. 2-6 players. All ages.
Should not have
• Cartoons, characters, people

```html
<!DOCTYPE html>
<html lang="en">
<head>
<meta charset="utf-8">
<title>The Lock Box – Escape Room Flyer</title>
<link href="https://fonts.googleapis.com/css2?family=Anton&family=Oswald:wght@400;500&family=Poppins:wght@300;600;700&family=Mulish:wght@400&display=swap" rel="stylesheet">
<style>
  :root {
    --paper: #ffffff;
    --ink: #3a3a3c;
    --panel: #3f3f41;
    --orange-deep: #c8742f;
    --orange-light: #f5b865;
    --photo-dark: #3b3632;
    --photo-light: #c9c7c4;
    --gear-dark: #6b4a24;
    --gear-light: #b98a4a;
    --divider: #7a7a7c;
  }
  * { margin: 0; padding: 0; box-sizing: border-box; }
  html, body { width: 869px; height: 1200px; overflow: hidden; background: var(--paper); }
  .flyer { position: relative; width: 869px; height: 1200px; background: var(--paper); font-family: "Poppins", sans-serif; }

  .hero-photo { position: absolute; left: 0; top: 0; width: 869px; height: 379px; }
  .hero-label {
    position: absolute; left: 464px; top: 14px; width: 270px;
    font-family: "Oswald", sans-serif; font-weight: 400; font-size: 46px;
    color: #f2efe6; letter-spacing: 1px; text-align: center; opacity: .9;
  }

  .brand { position: absolute; left: 40px; top: 130px; display: flex; align-items: center; gap: 12px; }
  .brand-dot { width: 30px; height: 30px; border-radius: 50%; background: var(--orange-deep); }
  .brand-name { font-family: "Oswald", sans-serif; font-weight: 500; font-size: 40px; color: var(--ink); text-transform: uppercase; }

  .headline {
    position: absolute; left: 33px; top: 318px;
    font-family: "Anton", sans-serif; font-size: 142px; line-height: 162px;
    background: linear-gradient(90deg, var(--orange-deep), var(--orange-light));
    -webkit-background-clip: text; background-clip: text; color: transparent;
    letter-spacing: 1px;
  }
  .headline-rule { position: absolute; left: 31px; top: 636px; width: 302px; height: 5px; background: var(--ink); }

  .tagline {
    position: absolute; left: 33px; top: 648px;
    font-family: "Oswald", sans-serif; font-weight: 500; font-size: 64px; line-height: 74px;
    color: var(--ink); text-transform: uppercase; letter-spacing: -.5px;
  }

  .intro {
    position: absolute; left: 34px; top: 808px; width: 402px;
    font-family: "Mulish", sans-serif; font-size: 17.3px; line-height: 26px;
    color: var(--ink); text-align: justify;
  }

  .features { position: absolute; left: 34px; top: 1014px; list-style: none; }
  .features li { display: flex; align-items: center; gap: 18px; height: 33px; font-weight: 600; font-size: 17px; color: var(--ink); text-transform: uppercase; }
  .features svg { width: 22px; height: 22px; }

  .web-bar {
    position: absolute; left: 0; top: 1146px; width: 478px; height: 54px;
    background: linear-gradient(90deg, var(--orange-deep), var(--orange-light));
    color: #fff; font-weight: 700; font-size: 21px; line-height: 54px; padding-left: 33px;
  }

  .rooms { position: absolute; left: 478px; top: 379px; width: 391px; height: 328px; background: var(--panel); color: #fff; padding: 56px 0 0 40px; }
  .rooms h2 { font-weight: 700; font-size: 28px; line-height: 32px; text-transform: uppercase; }
  .rooms p { font-weight: 300; font-size: 21px; margin-top: 6px; text-transform: uppercase; }
  .rooms hr { border: 0; height: 3px; width: 134px; background: var(--divider); margin: 10px 0 14px; }

  .first-band {
    position: absolute; left: 478px; top: 712px; width: 391px; height: 145px;
    background: linear-gradient(90deg, var(--orange-deep), var(--orange-light));
    border-top: 5px solid var(--paper); border-bottom: 6px solid var(--paper);
    font-family: "Oswald", sans-serif; font-weight: 500; font-size: 42px; line-height: 62px;
    color: #fff; text-transform: uppercase; padding: 6px 0 0 44px;
  }

  .contact { position: absolute; left: 478px; top: 857px; width: 391px; height: 343px; background: var(--panel); color: #fff; }
  .gears { position: absolute; left: 18px; top: 36px; width: 355px; height: 145px; }
  .contact h2 { position: absolute; left: 44px; top: 200px; font-weight: 700; font-size: 29px; text-transform: uppercase; }
  .phone { position: absolute; left: 43px; top: 253px; display: flex; align-items: center; gap: 22px; font-weight: 600; font-size: 28px; }
  .phone svg { width: 48px; height: 48px; }
</style>
</head>
<body>
<main class="flyer">
  <svg class="hero-photo" viewBox="0 0 869 379" role="img" aria-label="Moody photograph of a dark desk lamp lit against a grey wall">
    <defs>
      <linearGradient id="photoTone" x1="0" y1="0" x2="0.6" y2="1">
        <stop offset="0" stop-color="var(--photo-light)"/>
        <stop offset="1" stop-color="var(--photo-dark)"/>
      </linearGradient>
    </defs>
    <polygon points="241,0 869,0 869,379 478,379" fill="url(#photoTone)"/>
  </svg>
  <div class="hero-label">ESCAPE ROOM</div>

  <div class="brand">
    <span class="brand-dot"></span>
    <span class="brand-name">The Lock Box</span>
  </div>

  <h1 class="headline">ESCAPE<br>ROOM</h1>
  <div class="headline-rule"></div>

  <p class="tagline">Many will enter<br>few will escape</p>

  <p class="intro">Whether you are having a night out with friends or family, celebrating a special event, planning a team-building activity, or simply wanting a diversion from the doldrums of your workweek, The Lock Box will provide you an unforgettable live-action gaming experience.</p>

  <ul class="features">
    <li><svg viewBox="0 0 22 22"><circle cx="11" cy="11" r="10" fill="var(--ink)"/><circle cx="11" cy="11" r="6" fill="none" stroke="#fff" stroke-width="1.6"/><path d="M11 7v4l3 2" stroke="#fff" stroke-width="1.6" fill="none"/></svg>60 minute game.</li>
    <li><svg viewBox="0 0 22 22"><circle cx="11" cy="11" r="10" fill="var(--ink)"/><circle cx="11" cy="11" r="4" fill="none" stroke="#fff" stroke-width="2"/><path d="M11 3v3M11 16v3M3 11h3M16 11h3" stroke="#fff" stroke-width="2"/></svg>Team work.</li>
    <li><svg viewBox="0 0 22 22"><circle cx="11" cy="11" r="10" fill="var(--ink)"/><circle cx="11" cy="9" r="3" fill="#fff"/><path d="M5.5 17c1-3 3-4 5.5-4s4.5 1 5.5 4" fill="#fff"/></svg>2-6 player.</li>
    <li><svg viewBox="0 0 22 22"><circle cx="11" cy="11" r="10" fill="var(--ink)"/><circle cx="8" cy="7" r="2" fill="#fff"/><circle cx="14" cy="7" r="2" fill="#fff"/><rect x="6" y="10" width="4" height="7" rx="1" fill="#fff"/><rect x="12" y="10" width="4" height="7" rx="1" fill="#fff"/></svg>All ages.</li>
  </ul>

  <div class="web-bar">www.thelockboxhartwell.com</div>

  <section class="rooms">
    <h2>We have<br>1 room</h2>
    <p>The miller's shadows</p>
    <hr>
    <h2>A second room<br>coming soon</h2>
    <p>Varuna's Vault</p>
  </section>

  <div class="first-band">Hartwell's first<br>escape room</div>

  <section class="contact">
    <svg class="gears" viewBox="0 0 355 145" role="img" aria-label="Illustration of brass clockwork gears around a keyhole dial">
      <defs>
        <radialGradient id="gearTone" cx="0.5" cy="0.5" r="0.5">
          <stop offset="0" stop-color="var(--gear-light)"/>
          <stop offset="1" stop-color="var(--gear-dark)" stop-opacity="0.2"/>
        </radialGradient>
      </defs>
      <ellipse cx="177" cy="72" rx="175" ry="70" fill="url(#gearTone)"/>
    </svg>
    <h2>Contact us</h2>
    <div class="phone">
      <svg viewBox="0 0 48 48"><circle cx="24" cy="24" r="22" fill="none" stroke="#fff" stroke-width="2.5"/><path d="M17 12c2 0 3 5 3 6s-2 2-2 3c1 3 4 6 7 7 1 0 2-2 3-2s6 1 6 3-2 5-5 5c-8 0-16-8-16-16 0-3 2-6 4-6z" fill="none" stroke="#fff" stroke-width="2.2" stroke-linejoin="round"/></svg>
      <span>0417 265 839</span>
    </div>
  </section>
</main>
</body>
</html>
```